Allied Health Clinic needs catchy poster ad for lightbox

We need a catchy and effective poster designed for our retail lightbox which is in a busy corridor. We are a multi disciplinary sports injury clinic offering a range of allied health services. Established in 1999. We need people to understand our business identity and services clearly. I have come up with a very rough idea as far as what I think the copy should contain. The picture is an example of what image I am trying to convey to the potential client. I am not a designer clearly. We specialise in treating difficult problems.
Size of the poster is 451mm x 741mm at 300dpi. We will then blow the image up to double this size which will be good enough resolution for the printing.

Target Market(s)

White collar professionals - male and female, active 20-50 range

Industry/Entity Type

Healthcare

Font styles to use
Sans Serif

Requirements
Nice to have
• Easy to read, polished, nice tie in to my logo colours

```html
<!DOCTYPE html>
<html lang="en">
<head>
<meta charset="utf-8">
<title>Corefield Physiotherapy – Injury Experts</title>
<link href="https://fonts.googleapis.com/css2?family=Montserrat:wght@400;500;700;800;900&display=swap" rel="stylesheet">
<style>
  :root {
    --sky-dark: #23272c;
    --sky-mid: #5d5a55;
    --sky-glow: #c9b79a;
    --pitch: #2f4a26;
    --pitch-dark: #1f2a1b;
    --panel-dark: #2a2a2a;
    --green: #7ac142;
    --green-bright: #3ee032;
    --ink: #1d1d1d;
    --white: #ffffff;
    --headline-silver: #e9ecf3;
  }
  * { margin: 0; padding: 0; box-sizing: border-box; }
  html, body { width: 730px; height: 1200px; overflow: hidden; background: var(--white); }
  body { font-family: "Montserrat", sans-serif; }

  .poster { position: relative; width: 730px; height: 1200px; overflow: hidden; }

  .hero {
    position: absolute; left: 0; top: 0; width: 730px; height: 934px;
    background: linear-gradient(180deg, var(--sky-dark) 0%, var(--sky-mid) 22%, var(--sky-glow) 38%, #6c6258 50%, var(--pitch) 66%, var(--pitch-dark) 80%, var(--panel-dark) 100%);
  }

  .headline-injury {
    position: absolute; left: 44px; top: 22px;
    font-size: 150px; font-weight: 800; line-height: 1; letter-spacing: -2px;
    color: var(--headline-silver);
  }
  .headline-experts {
    position: absolute; left: 44px; top: 166px;
    font-size: 97px; font-weight: 900; line-height: 1; letter-spacing: -1px;
    color: var(--green-bright);
  }
  .tagline {
    position: absolute; left: 43px; top: 278px;
    font-size: 45px; font-weight: 800; line-height: 1.08;
    color: var(--ink);
  }
  .since {
    position: absolute; left: 42px; top: 632px;
    font-size: 25px; font-weight: 500; line-height: 1.35;
    color: var(--white);
  }
  .since strong { font-weight: 800; }

  .services-intro {
    position: absolute; left: 43px; top: 786px;
    font-size: 24px; font-weight: 400; color: var(--white);
  }
  .services {
    position: absolute; left: 42px; top: 827px;
    font-size: 26px; font-weight: 800; line-height: 1.3;
    color: var(--green);
  }
  .services .sep { font-weight: 400; color: var(--green); padding: 0 4px; }

  .footer {
    position: absolute; left: 0; top: 934px; width: 730px; height: 266px;
    background: var(--white);
  }
  .brand {
    position: absolute; left: 70px; top: 34px;
    display: flex; align-items: center; gap: 22px;
  }
  .brand-dot { width: 64px; height: 64px; border-radius: 50%; background: var(--green); flex: none; }
  .brand-name {
    font-size: 27px; font-weight: 700; line-height: 1.25; color: #555555;
  }
  .directions {
    position: absolute; left: 0; width: 730px; top: 172px;
    text-align: center; font-size: 27px; font-weight: 400; color: var(--ink);
  }
  .directions .level { background: var(--ink); color: var(--white); padding: 0 6px; }
  .contact {
    position: absolute; left: 0; width: 730px; top: 216px;
    display: flex; justify-content: center; align-items: center; gap: 18px;
    font-size: 25px; color: var(--ink);
  }
  .contact span { display: inline-flex; align-items: center; gap: 6px; }
  .contact svg { width: 20px; height: 20px; }
</style>
</head>
<body>
<main class="poster">
  <section class="hero" role="img" aria-label="Footballer kicking a ball in a floodlit stadium at dusk, with glowing highlights on his knees and ankle"></section>

  <h1 class="headline-injury">INJURY</h1>
  <p class="headline-experts">EXPERTS</p>
  <p class="tagline">TRUSTED BY<br>ATHLETES</p>

  <p class="since">SUCCESSFULLY TREATING<br>DIFFICULT INJURIES<br><strong>SINCE 1999</strong></p>

  <p class="services-intro">A Complete range of services</p>
  <p class="services">
    SPORTS PHYSIOTHERAPY<span class="sep">|</span>CHIROPRACTIC<br>
    MASSAGE<span class="sep">|</span>PODIATRY<span class="sep">|</span>EXERCISE PHYSIOLOGY
  </p>

  <footer class="footer">
    <div class="brand">
      <span class="brand-dot"></span>
      <span class="brand-name">Corefield Physiotherapy<br>&amp; Sports Injury Clinic</span>
    </div>
    <p class="directions">TAKE LIFTS TO <span class="level">LEVEL 8</span></p>
    <p class="contact">
      <span>
        <svg viewBox="0 0 24 24" aria-hidden="true"><path fill="currentColor" d="M6.6 10.8a15.1 15.1 0 0 0 6.6 6.6l2.2-2.2a1 1 0 0 1 1-.25 11.4 11.4 0 0 0 3.6.57 1 1 0 0 1 1 1V20a1 1 0 0 1-1 1A17 17 0 0 1 3 4a1 1 0 0 1 1-1h3.5a1 1 0 0 1 1 1c0 1.25.2 2.45.57 3.57a1 1 0 0 1-.25 1z"/></svg>
        8123 4567
      </span>
      <span>
        <svg viewBox="0 0 24 24" aria-hidden="true"><g fill="none" stroke="currentColor" stroke-width="1.8"><circle cx="12" cy="12" r="9"/><ellipse cx="12" cy="12" rx="4" ry="9"/><path d="M3 12h18M4.5 7.5h15M4.5 16.5h15"/></g></svg>
        corefieldphysioclinic.com.au
      </span>
    </p>
  </footer>
</main>
</body>
</html>
```